Brevik Law Client Handbook

We are a small, rapidly growing, criminal defense law firm located in a suburb of Seattle, WA. The cover should be professional and be consistent with our image a sleek, modern, and efficient. The included files show our designs used in other projects for reference.

```html
<!DOCTYPE html>
<html lang="en">
<head>
<meta charset="utf-8">
<title>Brevik Law Firm — Handbook Cover</title>
<link rel="stylesheet" href="https://fonts.googleapis.com/css2?family=Marcellus&family=Lato:wght@400&display=swap">
<style>
  :root {
    --backdrop: #758c99;
    --navy-top: #113a5a;
    --navy-bottom: #062c4a;
    --band: #0c3455;
    --band-edge: rgba(0, 15, 30, 0.45);
    --ink: #ffffff;
    --rule: #e9eef2;
  }
  * { margin: 0; padding: 0; box-sizing: border-box; }
  html, body {
    width: 1200px; height: 857px; overflow: hidden;
    background: var(--backdrop);
  }
  .canvas { position: relative; width: 1200px; height: 857px; }

  .cover, .spine {
    position: absolute; top: 118px; height: 617px;
    background: linear-gradient(180deg, var(--navy-top), var(--navy-bottom));
    overflow: hidden;
  }
  .cover { width: 421px; }
  .cover--back { left: 89px; }
  .cover--front { left: 677px; }
  .spine { left: 563px; width: 69px; }

  .bands { position: absolute; inset: 0; width: 100%; height: 100%; }

  .frame-line { position: absolute; background: var(--rule); }

  .wordmark { position: absolute; color: var(--ink); text-align: center; }
  .wordmark__name {
    font-family: "Marcellus", serif; font-size: 23px;
    letter-spacing: 0.32em; line-height: 1; margin-right: -0.32em;
  }
  .wordmark__sub {
    display: flex; align-items: center; justify-content: center; gap: 6px;
    font-family: "Lato", sans-serif; font-size: 9px; letter-spacing: 0.18em;
    margin-top: 3px;
  }
  .wordmark__sub::before, .wordmark__sub::after {
    content: ""; width: 22px; height: 1px; background: var(--ink);
  }

  .contact {
    position: absolute; left: 76px; top: 329px;
    font-family: "Lato", sans-serif; font-size: 6.6px; line-height: 9px;
    color: var(--ink);
  }
  .contact__web { margin-top: 9px; }

  .tagline {
    position: absolute; left: 221px; top: 331px; width: 168px;
    text-align: center; color: var(--ink);
    font-family: "Marcellus", serif; font-size: 9.5px; letter-spacing: 0.04em;
  }

  .spine__text {
    position: absolute; left: 50%; transform: translateX(-50%);
    writing-mode: vertical-rl; color: var(--ink); white-space: nowrap;
  }
  .spine__name {
    top: 130px; font-family: "Marcellus", serif; font-size: 19px; letter-spacing: 0.34em;
    left: 60%;
  }
  .spine__sub {
    top: 143px; left: 36%; font-family: "Lato", sans-serif; font-size: 7px; letter-spacing: 0.2em;
  }
  .spine__title {
    top: 284px; font-family: "Marcellus", serif; font-size: 19px; letter-spacing: 0.02em;
  }
</style>
</head>
<body>
<main class="canvas">

  <section class="cover cover--back" aria-label="Back cover">
    <svg class="bands" viewBox="0 0 421 617" preserveAspectRatio="none" aria-hidden="true">
      <polygon points="80,0 180,0 421,300 421,430" fill="var(--band)" stroke="var(--band-edge)" stroke-width="1.5"/>
      <polygon points="0,470 120,330 160,380 40,617 0,617" fill="var(--band)" stroke="var(--band-edge)" stroke-width="1.5"/>
    </svg>
    <div class="frame-line" style="left:78px; top:34px; width:137px; height:1.2px;"></div>
    <div class="frame-line" style="left:78px; top:34px; width:1.2px; height:80px;"></div>
    <div class="frame-line" style="left:78px; top:500px; width:1.2px; height:90px;"></div>
    <div class="frame-line" style="left:78px; top:589px; width:133px; height:1.2px;"></div>

    <div class="wordmark" style="left:74px; top:282px;">
      <div class="wordmark__name">BREVIK</div>
      <div class="wordmark__sub">LAW FIRM</div>
    </div>
    <address class="contact" style="font-style:normal;">
      2150 Harbor View Ave NE<br>
      Suite 410<br>
      Redmond, WA 98052
      <div class="contact__web">www.breviklawfirm.com</div>
    </address>
  </section>

  <section class="spine" aria-label="Spine">
    <div class="spine__text spine__name">BREVIK</div>
    <div class="spine__text spine__sub">LAW FIRM</div>
    <div class="spine__text spine__title">FOR LAW ENFORCEMENT</div>
  </section>

  <section class="cover cover--front" aria-label="Front cover">
    <svg class="bands" viewBox="0 0 421 617" preserveAspectRatio="none" aria-hidden="true">
      <polygon points="230,0 345,0 80,617 0,617 0,500" fill="var(--band)" stroke="var(--band-edge)" stroke-width="1.5"/>
      <polygon points="421,420 421,560 360,617 250,617" fill="var(--band)" stroke="var(--band-edge)" stroke-width="1.5"/>
    </svg>
    <div class="frame-line" style="left:209px; top:31px; width:183px; height:1.2px;"></div>
    <div class="frame-line" style="left:391px; top:31px; width:1.2px; height:28px;"></div>
    <div class="frame-line" style="left:391px; top:558px; width:1.2px; height:30px;"></div>
    <div class="frame-line" style="left:209px; top:587px; width:183px; height:1.2px;"></div>
    <div class="frame-line" style="left:28px; top:251px; width:1.2px; height:111px;"></div>

    <div class="wordmark" style="left:230px; top:286px; width:160px;">
      <div class="wordmark__name">BREVIK</div>
      <div class="wordmark__sub">LAW FIRM</div>
    </div>
    <div class="tagline">FOR LAW ENFORCEMENT</div>
  </section>

</main>
</body>
</html>
```